NEW YORK Plumbing/utility company 10 year anniversary business card

Looking For simple back and front business card would like to include a few things in description
We offer 24/7 emergency service
residential
commercial
industrial
municipal
services offered
Plumbing
hydro excavation
hydro jetting
Well pumps
Sewer pumps
water mains
sewer mains

```html
<!DOCTYPE html>
<html lang="en">
<head>
<meta charset="utf-8">
<title>Ridgeline Water &amp; Sewer – Business Card</title>
<link rel="stylesheet" href="https://fonts.googleapis.com/css2?family=Montserrat:wght@300;400;500;600&family=Open+Sans:wght@400;600;700&display=swap">
<style>
  :root {
    --backdrop: #262626;
    --card-top: #1c1c1c;
    --card-bottom: #050505;
    --brand-blue: #0a6ab0;
    --bright-blue: #1f8fe0;
    --accent-red: #e3242b;
    --text-white: #ffffff;
    --text-soft: #d4d4d4;
    --text-grey: #a8a8a8;
  }
  * { margin: 0; padding: 0; box-sizing: border-box; }
  html, body { width: 1200px; height: 780px; overflow: hidden; }
  body {
    background: var(--backdrop);
    position: relative;
    font-family: "Open Sans", sans-serif;
    color: var(--text-white);
  }
  .card {
    position: absolute;
    top: 230px;
    width: 560px;
    height: 320px;
    border-radius: 28px;
    background: radial-gradient(ellipse at 40% 30%, var(--card-top), var(--card-bottom) 75%);
    overflow: hidden;
    box-shadow: 0 18px 40px rgba(0,0,0,0.55);
  }
  .card--front { left: 20px; }
  .card--back { left: 620px; }

  .brand-name {
    position: absolute;
    display: flex;
    align-items: center;
    gap: 10px;
    font-family: "Open Sans", sans-serif;
    font-weight: 700;
    color: var(--text-soft);
    line-height: 1.05;
    letter-spacing: 0.5px;
  }
  .brand-name__dot {
    width: 16px; height: 16px; border-radius: 50%;
    background: var(--bright-blue);
    flex: none;
  }
  .card--front .brand-name { left: 40px; top: 92px; font-size: 24px; }
  .card--back .brand-name { left: 36px; top: 36px; font-size: 22px; }

  .divider {
    position: absolute;
    left: 258px; top: 42px;
    width: 2px; height: 150px;
    background: var(--accent-red);
  }
  .contact {
    position: absolute;
    left: 282px; top: 38px;
    font-family: "Montserrat", sans-serif;
  }
  .contact__name {
    font-size: 20px; font-weight: 600;
    color: var(--brand-blue);
    letter-spacing: 0.3px;
  }
  .contact__role {
    font-size: 17px; font-weight: 300;
    color: var(--text-grey);
    margin-bottom: 6px;
  }
  .contact__address {
    font-size: 10.5px; font-weight: 500;
    color: var(--text-soft);
    line-height: 1.35;
    margin-bottom: 4px;
  }
  .contact__row {
    display: flex; align-items: center; gap: 8px;
    font-size: 10.5px; font-weight: 500;
    color: var(--text-soft);
    line-height: 1.7;
  }
  .contact__row svg { width: 12px; height: 12px; flex: none; }

  .band {
    position: absolute;
    left: 0; right: 0;
    top: 214px; height: 32px;
    background: var(--brand-blue);
  }
  .band__text {
    position: absolute;
    left: 200px; top: 2px;
    font-size: 19px; font-weight: 700;
    white-space: nowrap;
  }

  .back-band {
    position: absolute;
    left: 230px; top: 76px;
    width: 330px; height: 34px;
  }
  .back-band__text {
    position: absolute;
    right: 22px; top: 80px;
    font-size: 17px; font-weight: 700;
    white-space: nowrap;
  }
  .services-title {
    position: absolute;
    left: 46px; top: 124px;
    font-size: 21px; font-weight: 600;
    color: var(--bright-blue);
  }
  .services-list {
    position: absolute;
    left: 52px; top: 158px;
    list-style: none;
    font-size: 13px; line-height: 19px;
    color: var(--text-white);
  }
  .sectors-list {
    position: absolute;
    left: 262px; top: 122px;
    list-style: none;
    font-size: 25px; line-height: 31px;
    color: var(--text-white);
  }
  .services-list li, .sectors-list li {
    position: relative;
    padding-left: 16px;
  }
  .services-list li::before, .sectors-list li::before {
    content: "";
    position: absolute;
    left: 0; top: 50%;
    width: 6px; height: 6px; border-radius: 50%;
    background: var(--accent-red);
    transform: translateY(-50%);
  }
  .sectors-list li { padding-left: 22px; }
  .sectors-list li::before { width: 9px; height: 9px; }
</style>
</head>
<body>

<section class="card card--front" aria-label="Business card front">
  <div class="brand-name"><span class="brand-name__dot"></span><span>Ridgeline<br>Water &amp; Sewer</span></div>
  <div class="divider"></div>
  <div class="contact">
    <p class="contact__name">HARLAN VOSS</p>
    <p class="contact__role">Owner</p>
    <p class="contact__address">Unit 4/112<br>Kingsbridge Road,<br>Millbrook Plaza</p>
    <p class="contact__row">
      <svg viewBox="0 0 24 24"><path fill="var(--bright-blue)" d="M6.6 10.8a15 15 0 0 0 6.6 6.6l2.2-2.2a1 1 0 0 1 1-.25 11.4 11.4 0 0 0 3.6.57 1 1 0 0 1 1 1V20a1 1 0 0 1-1 1A17 17 0 0 1 3 4a1 1 0 0 1 1-1h3.5a1 1 0 0 1 1 1c0 1.250.2 2.45.57 3.57a1 1 0 0 1-.25 1z"/></svg>
      0400 555 018</p>
    <p class="contact__row">
      <svg viewBox="0 0 24 24"><rect x="2" y="5" width="20" height="14" rx="1" fill="var(--bright-blue)"/><path d="M3 6l9 7 9-7" fill="none" stroke="#050505" stroke-width="1.6"/></svg>
      office@ridgelinewater.com</p>
    <p class="contact__row">
      <svg viewBox="0 0 24 24" fill="none" stroke="var(--bright-blue)" stroke-width="1.8"><circle cx="12" cy="12" r="9"/><path d="M3 12h18M12 3c3 3 3 15 0 18M12 3c-3 3-3 15 0 18"/></svg>
      www.ridgelinewater.com</p>
  </div>
  <div class="band"><span class="band__text">We offer 24/7 emergency service</span></div>
</section>

<section class="card card--back" aria-label="Business card back">
  <div class="brand-name"><span class="brand-name__dot"></span><span>Ridgeline<br>Water &amp; Sewer</span></div>
  <svg class="back-band" viewBox="0 0 330 34" preserveAspectRatio="none" aria-hidden="true">
    <path d="M0 0 H330 V34 H22 Q12 34 8 20 Q5 6 0 0 Z" fill="var(--brand-blue)"/>
  </svg>
  <p class="back-band__text">We offer 24/7 emergency service</p>
  <h2 class="services-title">Services Offered</h2>
  <ul class="services-list">
    <li>Plumbing</li>
    <li>Hydro excavation</li>
    <li>Hydro jetting</li>
    <li>Well pumps</li>
    <li>Sewer pumps</li>
    <li>Water mains</li>
    <li>Sewer mains</li>
  </ul>
  <ul class="sectors-list">
    <li>residential</li>
    <li>commercial</li>
    <li>industrial</li>
    <li>municipal</li>
  </ul>
</section>

</body>
</html>
```